Brightwell PC Help - Web Page
Remote Tech Support Provider
Brightwell PC Help - Web Page -
Creative Brief
24/7 remote PC support. Simple pricing and premium service supporting small business and consumers in the US.
Monthly service plans will be the emphasis but will also provide pay per incident support. Multiple computer discounts will be available and service plans will be structured as follows:
-- $19.99 for upto 3 computers
-- $34.99 for upto 5 computers
-- $79.00 for 10 computers
-- More than 10 computers, call for an instant quote.
KEY OFFERING:
* Automated UNLIMITED Online Backup as an add on for $5/month
Core focus will be on restoring the speed of your computer, removing viruses/malware etc. Will also help users with their WiFi Security Setup, printers, MP3 players, cameras, System Recovery Quillstone Suite, Email and Calendaring Setup, Domain Registration, Web Content Filtering Configuration,
Alternative Software Solution Recommendations... -- ALL for the same monthly fee.
MUST be 100% CSS for me to consider the submission. Prefer clean and simple over cluttered and complex. Every page will have a link that is up front and visible to take you to the order page.
www.vaultmerrow.example
www.helpquorn.example
www.dravelline.example

```html
<!DOCTYPE html>
<html lang="en">
<head>
<meta charset="utf-8">
<title>Brightwell PC Help – 24/7 Remote PC Support</title>
<link rel="stylesheet" href="https://fonts.googleapis.com/css2?family=Arimo:wght@400;700&display=swap">
<style>
:root{
  --header-dark:#1f1f1f;
  --header-mid:#3a3a3a;
  --nav-text:#f2f2f2;
  --pill:#d9d9d9;
  --panel-edge:#b9b9b9;
  --ink:#2b2b2b;
  --green:#8cc63f;
  --green-dark:#5f9a1c;
  --green-light:#c6e58e;
  --orange:#f47b20;
  --orange-light:#f9a14b;
  --social-blue:#3b5b98;
  --social-sky:#4fb3e8;
  --lower-band:#6b6b6b;
  --lower-light:#dcdcdc;
  --footer:#2a2a2a;
  --white:#ffffff;
}
*{box-sizing:border-box;margin:0;padding:0}
html,body{width:1200px;height:931px;overflow:hidden}
body{font-family:"Arimo",Arial,sans-serif;color:var(--ink);
  background:linear-gradient(180deg,var(--header-dark) 0,var(--header-mid) 190px,#8a8a8a 500px,#cfcfcf 660px,var(--lower-light) 660px);
  position:relative}
.site-header{position:absolute;left:0;top:0;width:1200px;height:130px}
.brand{position:absolute;left:140px;top:34px;display:flex;align-items:center;gap:14px}
.brand-mark{width:40px;height:40px;background:var(--green)}
.brand-name{font-size:34px;font-weight:700;color:var(--green);letter-spacing:-0.5px}
.follow{position:absolute;right:140px;top:22px;display:flex;align-items:center;gap:8px;color:var(--white);font-size:17px}
.social{font-size:11px;color:var(--white);padding:4px 9px;border-radius:2px}
.social.friendwall{background:var(--social-blue)}
.social.chirpline{background:var(--social-sky)}
.hotline{position:absolute;right:140px;top:66px;color:var(--white);font-size:19px}
.main-nav{position:absolute;left:0;top:143px;width:1200px;height:34px}
.main-nav a{position:absolute;top:7px;color:var(--nav-text);font-size:14px;font-weight:700;text-decoration:none}
.main-nav a.current{top:1px;padding:6px 14px;background:var(--pill);color:var(--ink);border-radius:14px}
.hero{position:absolute;left:121px;top:201px;width:958px;height:292px;border:3px solid var(--panel-edge);
  background:linear-gradient(180deg,#ffffff,#e6e6e6);}
.hero-title{position:absolute;left:20px;top:28px;font-size:31px;font-weight:400;color:var(--ink);white-space:nowrap}
.hero-title b{font-weight:700}
.hero-sub{position:absolute;left:52px;top:70px;font-size:24px;color:var(--ink);white-space:nowrap}
.price-list{position:absolute;left:158px;top:116px;list-style:none}
.price-list li{display:flex;align-items:center;gap:10px;font-size:16px;height:32px}
.offer-badge{position:absolute;left:0;top:151px;width:156px;height:138px;border-radius:0 70px 70px 0;
  background:radial-gradient(circle at 50% 40%,var(--orange-light),var(--orange));color:var(--white);text-align:center;padding-top:18px}
.offer-badge .big{font-size:16px;font-weight:700;display:block}
.offer-badge .small{font-size:14px;display:block}
.offer-badge .just{position:absolute;left:12px;top:84px;font-size:12px;transform:rotate(-20deg)}
.offer-badge .amount{position:absolute;left:68px;top:62px;font-size:46px;font-weight:700}
.cta{position:absolute;left:176px;top:217px;width:163px;height:45px;border-radius:23px;
  background:linear-gradient(180deg,var(--green-light),var(--green));display:flex;align-items:center;gap:8px;padding-left:12px;text-decoration:none}
.cta-icon{width:30px;height:30px;border-radius:50%;background:var(--white);flex:none}
.cta-text{color:var(--white);font-weight:700;font-size:17px;line-height:1}
.cta-text small{display:block;font-size:9px;font-weight:400}
.devices{position:absolute;left:522px;top:18px;width:428px;height:194px;
  background:linear-gradient(135deg,#d0d0d0,#7d9fcf 60%,#e5e5e5)}
.hero-tagline{position:absolute;right:22px;top:240px;font-size:25px;white-space:nowrap}
.hero-tagline b{font-weight:700}
.services{position:absolute;left:121px;top:513px;width:958px;height:136px;border:3px solid var(--panel-edge);
  background:linear-gradient(180deg,var(--green-light),var(--green));display:flex;justify-content:space-around;padding:10px 40px 0}
.service{width:150px;text-align:center}
.service-art{width:70px;height:70px;margin:0 auto 12px;border-radius:8px;background:linear-gradient(135deg,#f1f1f1,#7f9db0)}
.service-name{font-size:12px;line-height:1.2;color:var(--ink)}
.lower{position:absolute;left:0;top:667px;width:1200px;height:201px;background:linear-gradient(180deg,#a5a5a5,var(--lower-band))}
.lower-brand{position:absolute;left:131px;top:12px;width:246px;height:86px;background:linear-gradient(180deg,#f2f2f2,#c9c9c9);
  display:flex;align-items:center;justify-content:center;gap:8px}
.lower-brand .brand-mark{width:22px;height:22px;background:#8c8c8c}
.lower-brand .brand-name{font-size:20px;color:#7a7a7a}
.subscribe{position:absolute;left:131px;top:103px;width:246px;height:30px;border-radius:4px;background:var(--footer);
  color:var(--white);font-size:12px;display:flex;align-items:center;gap:8px;padding-left:12px}
.subscribe svg{flex:none}
.plans{position:absolute;left:420px;top:14px;width:650px;color:var(--white);font-size:13px;line-height:1.45}
.plans ul{list-style:none;margin-top:14px}
.plans li{height:30px;display:flex;align-items:center;gap:10px}
.site-footer{position:absolute;left:0;top:868px;width:1200px;height:63px;background:var(--footer);text-align:center}
.footer-nav{padding-top:10px}
.footer-nav a{color:#cfcfcf;font-size:12px;text-decoration:none;margin:0 14px}
.copyright{color:#9a9a9a;font-size:11px;margin-top:10px}
</style>
</head>
<body>
<header class="site-header">
  <div class="brand"><span class="brand-mark"></span><span class="brand-name">brightwellpchelp.com</span></div>
  <div class="follow">Follow us on <span class="social friendwall">Friendwall</span><span class="social chirpline">Chirpline</span></div>
  <div class="hotline">Call here for problem solved (000) 555-0142</div>
</header>

<nav class="main-nav">
  <a class="current" style="left:184px">Home</a>
  <a style="left:307px">Who We Are</a>
  <a style="left:430px">How It Works</a>
  <a style="left:594px">Start Your Free Trial</a>
  <a style="left:788px">Buy</a>
  <a style="left:870px">Client Testimonials</a>
  <a style="left:1031px">Contact Us</a>
</nav>

<section class="hero">
  <h1 class="hero-title"><b>24/7</b> Remote PC support</h1>
  <p class="hero-sub">Simple <b>pricing</b> and <b>premium service</b></p>
  <ul class="price-list">
    <li><svg width="18" height="16" viewBox="0 0 18 16"><path d="M2 8l5 5L16 2" fill="none" stroke="#5f9a1c" stroke-width="4"/></svg>$19.99 for upto 3 computers</li>
    <li><svg width="18" height="16" viewBox="0 0 18 16"><path d="M2 8l5 5L16 2" fill="none" stroke="#5f9a1c" stroke-width="4"/></svg>$34.99 for upto 5 computers</li>
    <li><svg width="18" height="16" viewBox="0 0 18 16"><path d="M2 8l5 5L16 2" fill="none" stroke="#5f9a1c" stroke-width="4"/></svg>$79.00 for 10 computers</li>
  </ul>
  <div class="offer-badge">
    <span class="big">UNLIMITED</span><span class="small">Online Backup</span>
    <span class="just">Just for</span><span class="amount">$5</span>
  </div>
  <a class="cta"><span class="cta-icon"></span><span class="cta-text">CALL NOW<small>and make appointment</small></span></a>
  <div class="devices" role="img" aria-label="Desktop computer, laptop and phone showing remote support"></div>
  <p class="hero-tagline"><b>Desktop, PC/Laptop, WiFi Security</b> and <b>Recovery</b></p>
</section>

<section class="services">
  <div class="service"><div class="service-art" role="img" aria-label="Shield icon for virus removal"></div><p class="service-name">Virus Spy and<br>Malware Removal</p></div>
  <div class="service"><div class="service-art" role="img" aria-label="Books icon for tutoring"></div><p class="service-name">Tutoring Sessions<br>and Packages</p></div>
  <div class="service"><div class="service-art" role="img" aria-label="Router and printer icon"></div><p class="service-name">Wireless Networking<br>and Printing</p></div>
  <div class="service"><div class="service-art" role="img" aria-label="Hard drive icon for data recovery"></div><p class="service-name">Data Recovery &amp;<br>Backup Solutions</p></div>
  <div class="service"><div class="service-art" role="img" aria-label="Software installation icon"></div><p class="service-name">New Quillstone Suite<br>Installation</p></div>
</section>

<section class="lower">
  <div class="lower-brand"><span class="brand-mark"></span><span class="brand-name">brightwellpchelp.com</span></div>
  <div class="subscribe"><svg width="16" height="12" viewBox="0 0 16 12"><rect x="0.5" y="0.5" width="15" height="11" fill="none" stroke="#fff"/><path d="M1 1l7 6 7-6" fill="none" stroke="#fff"/></svg>Enter your email ID for subscribe</div>
  <div class="plans">
    <p>Monthly service plans will be the emphasis but will also provide pay per incident support. Multiple computer discounts will be available and service plans will be structured as follows:</p>
    <ul>
      <li><svg width="8" height="10" viewBox="0 0 8 10"><path d="M0 0l8 5-8 5z" fill="#fff"/></svg>$19.99 for upto 3 computers</li>
      <li><svg width="8" height="10" viewBox="0 0 8 10"><path d="M0 0l8 5-8 5z" fill="#fff"/></svg>$34.99 for upto 5 computers</li>
      <li><svg width="8" height="10" viewBox="0 0 8 10"><path d="M0 0l8 5-8 5z" fill="#fff"/></svg>$79.00 for 10 computers</li>
      <li><svg width="8" height="10" viewBox="0 0 8 10"><path d="M0 0l8 5-8 5z" fill="#fff"/></svg>More than 10 computers, call for an instant quote.</li>
    </ul>
  </div>
</section>

<footer class="site-footer">
  <nav class="footer-nav"><a>Home</a><a>Who We Are</a><a>How It Works</a><a>Start Your Free Trial</a><a>Buy</a><a>Client Testimonials</a><a>Contact Us</a></nav>
  <p class="copyright">Copyright © 2011, Brightwell PC Help. All rights Reserved</p>
</footer>
</body>
</html>
```